RTBW Core Values

Core Values poster, A fun poster that has a light feel that clearly shows the five values.

Customer 1st, Loyalty, Education, quAlity, Respect.

If it works making the letters that spell out CLEAR jump out a little.

Industry/Entity Type

Education

```html
<!DOCTYPE html>
<html lang="en">
<head>
<meta charset="utf-8">
<title>RTBW Core Values</title>
<link rel="stylesheet" href="https://fonts.googleapis.com/css2?family=Open+Sans:wght@300;400;600&display=swap">
<style>
  :root {
    --lime: #d8e020;
    --yellow: #f1ee6a;
    --orange: #f6a83c;
    --sky: #3cbef0;
    --teal: #92cfc4;
    --cream: #fffcef;
    --value-red: #c8283a;
    --initial-black: #111111;
    --ink: #1a1a1a;
    --brand-red: #c8283a;
  }
  * { margin: 0; padding: 0; box-sizing: border-box; }
  html, body { width: 848px; height: 1200px; overflow: hidden; }
  .poster {
    position: relative;
    width: 848px;
    height: 1200px;
    overflow: hidden;
    font-family: "Open Sans", Arial, sans-serif;
    background:
      radial-gradient(ellipse 300px 280px at 640px 770px, rgba(255,253,245,0.98), rgba(255,253,245,0) 75%),
      radial-gradient(ellipse 330px 260px at 640px 500px, rgba(60,190,240,0.95), rgba(60,190,240,0) 75%),
      radial-gradient(ellipse 340px 420px at 140px 820px, rgba(146,207,196,0.95), rgba(146,207,196,0) 80%),
      radial-gradient(ellipse 230px 260px at 250px 400px, rgba(246,168,60,0.85), rgba(246,168,60,0) 75%),
      radial-gradient(ellipse 360px 420px at 880px 140px, rgba(246,168,60,0.95), rgba(246,168,60,0) 75%),
      radial-gradient(ellipse 320px 260px at 560px 160px, rgba(255,252,239,0.9), rgba(255,252,239,0) 75%),
      radial-gradient(ellipse 300px 320px at 880px 1100px, rgba(246,168,60,0.9), rgba(246,168,60,0) 75%),
      radial-gradient(ellipse 200px 260px at 0px 1160px, rgba(255,252,239,0.9), rgba(255,252,239,0) 75%),
      radial-gradient(ellipse 500px 500px at 420px 560px, var(--yellow), rgba(241,238,106,0) 85%),
      var(--lime);
  }
  .value {
    position: absolute;
    white-space: nowrap;
    color: var(--value-red);
    font-weight: 400;
    line-height: 1;
  }
  .value .initial {
    display: inline-block;
    color: var(--initial-black);
    font-weight: 600;
    font-size: 1.28em;
  }
  .value--customer { left: 88px; top: 56px; font-size: 52px; }
  .value--loyalty { left: 192px; top: 146px; font-size: 52px; }
  .value--education { left: 254px; top: 266px; font-size: 56px; }
  .value--education .initial { transform: rotate(-12deg); }
  .value--quality { left: 395px; top: 366px; font-size: 54px; }
  .value--respect { left: 542px; top: 470px; font-size: 54px; }
  .value--respect .initial { transform: rotate(-6deg); }

  .headline {
    position: absolute;
    left: 201px;
    top: 618px;
    font-size: 56px;
    font-weight: 300;
    color: var(--ink);
    letter-spacing: -0.5px;
    white-space: nowrap;
  }

  .brand {
    position: absolute;
    right: 56px;
    top: 1084px;
    text-align: right;
  }
  .brand__name {
    font-size: 46px;
    font-weight: 600;
    color: var(--brand-red);
    line-height: 1;
    letter-spacing: 2px;
  }
  .brand__tagline {
    margin-top: 8px;
    font-size: 19px;
    font-weight: 400;
    color: var(--ink);
    word-spacing: 3px;
    white-space: nowrap;
  }
</style>
</head>
<body>
<main class="poster">
  <p class="value value--customer"><span class="initial">C</span>ustomer 1st</p>
  <p class="value value--loyalty"><span class="initial">L</span>oyality</p>
  <p class="value value--education"><span class="initial">E</span>ducation</p>
  <p class="value value--quality">qu<span class="initial">A</span>lity</p>
  <p class="value value--respect"><span class="initial">R</span>espect</p>

  <h1 class="headline">Clear Core Values.</h1>

  <div class="brand">
    <p class="brand__name">RTBW</p>
    <p class="brand__tagline">Learn. Grow. Lead.</p>
  </div>
</main>
</body>
</html>
```